Simple but elegant business card/logo design for exclusive beauty business

We need a logo designed for a new elegant and exclusive beauty business called "R". The logo itself should be a stylistic and custom design for the letter "R". We would like the business card to have the logo as the centrepiece on a clean background. Gold Logo on black background or silver on white background.

The business card details should be displayed centre of the card. Details are as follows:

Tamsin Earle
Facebook: /shinesoftlyr
Instagram: /shinesoftlyr

The words "Shine Softly" should also appear somewhere on the card.

Industry/Entity Type

Business

Logo Text

G

Requirements
Must have
• Design must be simple, clean and elegant
Should not have
• The design should not be cluttered

```html
<!DOCTYPE html>
<html lang="en">
<head>
<meta charset="utf-8">
<title>Tamsin Earle — Business Card</title>
<link rel="stylesheet" href="https://fonts.googleapis.com/css2?family=Open+Sans:wght@400;700&family=Indie+Flower&display=swap">
<style>
  :root {
    --backdrop: #3b342f;
    --card: #0d0d0d;
    --card-edge: #1c1c1c;
    --gold: #f2b01e;
    --gold-line: #a37812;
    --silver: #d4d4d4;
    --lime: #9cc43a;
    --white: #f2f2f2;
  }
  * { margin: 0; padding: 0; box-sizing: border-box; }
  html, body {
    width: 1200px; height: 900px; overflow: hidden;
    background: var(--backdrop);
  }
  .canvas {
    position: relative; width: 1200px; height: 900px;
    display: flex; align-items: center; justify-content: center; gap: 50px;
  }
  .card {
    position: relative; width: 525px; height: 300px;
    background: var(--card);
    border: 1px solid var(--card-edge);
    box-shadow: 0 14px 30px rgba(0,0,0,0.45);
    font-family: "Open Sans", Arial, sans-serif;
  }
  /* Front side */
  .card-front .brand-mark {
    position: absolute; left: 70px; top: 50%; transform: translateY(-50%);
    width: 130px; text-align: center;
    font-weight: 700; font-size: 150px; line-height: 1;
    color: var(--gold);
  }
  .card-front .divider {
    position: absolute; left: 238px; top: 70px; width: 1px; height: 160px;
    background: linear-gradient(var(--gold-line), transparent 95%);
  }
  .card-front .details {
    position: absolute; left: 268px; top: 96px;
  }
  .details .name {
    font-weight: 700; font-size: 17px; letter-spacing: 0.3px;
    color: var(--gold); text-transform: uppercase; margin-bottom: 14px;
  }
  .details .handle {
    display: flex; align-items: center; gap: 8px;
    font-size: 14px; color: var(--white); line-height: 1.6;
  }
  .handle .dot {
    width: 12px; height: 12px; border-radius: 50%; background: var(--gold);
    flex: none;
  }
  /* Back side */
  .card-back .brand-mark {
    position: absolute; left: 0; right: 0; top: 40px; text-align: center;
    font-weight: 700; font-size: 130px; line-height: 1;
    color: var(--silver);
  }
  .card-back .tagline {
    position: absolute; left: 0; right: 0; top: 200px; text-align: center;
    font-family: "Indie Flower", cursive;
    font-size: 30px; color: var(--lime);
  }
</style>
</head>
<body>
  <main class="canvas">
    <section class="card card-front" aria-label="Card front">
      <div class="brand-mark">R</div>
      <div class="divider"></div>
      <div class="details">
        <p class="name">Tamsin Earle</p>
        <p class="handle"><span class="dot"></span>/shinesoftlyr</p>
        <p class="handle"><span class="dot"></span>/shinesoftlyr</p>
      </div>
    </section>
    <section class="card card-back" aria-label="Card back">
      <div class="brand-mark">R</div>
      <p class="tagline">Shine Softly</p>
    </section>
  </main>
</body>
</html>
```